Meditations CD Cover
Zielgruppe
Wir unterstützen Therapeuten ihre Praxis aufzubauen.
Aufgabenstellung
Ich wünsche einen CD Cover mit Rückseite und CD Druck, wo nicht zu esoterisch aussieht. Bitte keine Buddha, Steine, Yoga, Lotusblume!
ich hätte gerne mein Bild im Vordergrund, nicht zu prominent, klar strukturiert und nicht zu schwer, lieber mehr Platz lassen.
ich hätte gerne eine CD Jewel Cases.
Bitte eine ganz neutralle CD ohne das Grün von der Website. (sonnen-kern-werk.ch)
Die Meditation ist eine Mischung zwischen Business und Meditation, es geht um Kundenfindung.
Etwas schlichtes und modernes.
Was rauf muss:
CD Cover
Mirela Gantenbein-Rusch
Mein Foto
Titel:
Finde Deinen Kompass, Pfad der Stille!
bitte auch schreiben: die ÜBUNGS-CD zum Buch
Logo und mein Bild, nicht zu prominent!!!!
Beispiel: http://lunavertomiel.com/
http://www.bildquello.com/vector/electric-bulb-16125607?st=0561491
http://www.bildquello.com/vector/dart-board-16126309?st=425cf59
http://klangwiese-audio.com/tarnow-lukas-neue-pfade-zu-glueck-ruhe-und-freude-cd
Rückseite:
mein Foto und der Text:
Gehen Sie in die Resonanz und finden Sie den richtigen Klienten.
Gerne unterstütze ich Sie auf diesem wundervollen Weg ...
Mein Name ist Mirela Gantenbein, ich bin erfolgreiche Unternehmerin, die zugleich spiri- tuell denkt und handelt. Und ich bin fest davon überzeugt. Es gibt eine innere Kraft, die nicht nur Berge versetzt. Sondern auch Ihre Praxis fullt.
Auf dieser CD werden Sie angeleitet sich mit ihrem Idealkunden zu treffen. Sie werden entdecken welche Probleme oder Herausforderungen, Wünsche und Ziele Ihr potenzieller Klient.
Vielen Dank und viel Spass :-)

```html
<!DOCTYPE html>
<html lang="de">
<head>
<meta charset="utf-8">
<title>Übungs-CD – Finde Deinen Kompass</title>
<link href="https://fonts.googleapis.com/css2?family=Questrial&display=swap" rel="stylesheet">
<style>
  :root {
    --page: #ffffff;
    --purple-deep: #5a0f4c;
    --purple-mid: #8a1c74;
    --purple-glow: #b2389a;
    --magenta: #c23a9e;
    --pink-soft: #e3a6d6;
    --pink-label: #d55cb6;
    --white: #ffffff;
    --spine: #ffffff;
    --ink: #1c1c1c;
    --photo-light: #e4e0e2;
    --photo-dark: #3a3436;
  }
  * { margin: 0; padding: 0; box-sizing: border-box; }
  html, body { width: 1200px; height: 520px; overflow: hidden; background: var(--page); }
  body { font-family: "Questrial", "Century Gothic", sans-serif; position: relative; }

  .back-tray {
    position: absolute; left: 44px; top: 0; width: 624px; height: 479px;
    background: var(--spine);
    box-shadow: 3px 4px 5px rgba(0,0,0,.35);
  }
  .back-face {
    position: absolute; left: 32px; top: 0; width: 560px; height: 479px; overflow: hidden;
  }
  .network-bg {
    position: absolute; inset: 0;
    background:
      radial-gradient(ellipse at 50% 40%, var(--purple-glow) 0%, transparent 55%),
      radial-gradient(circle at 85% 20%, rgba(230,170,225,.45) 0%, transparent 30%),
      radial-gradient(circle at 10% 80%, rgba(230,170,225,.4) 0%, transparent 30%),
      linear-gradient(160deg, var(--purple-mid), var(--purple-deep));
  }
  .spine-label {
    position: absolute; top: 240px; font-size: 10.5px; font-weight: bold;
    color: var(--ink); white-space: nowrap; letter-spacing: .2px;
  }
  .spine-left { left: 15px; transform: translate(-50%, -50%) rotate(-90deg); }
  .spine-right { left: 607px; transform: translate(-50%, -50%) rotate(90deg); }

  .back-copy p {
    position: absolute; color: var(--white); font-size: 11.6px; line-height: 14.4px;
  }
  .intro { left: 73px; top: 61px; }
  .about { left: 105px; top: 132px; }
  .cd-info { left: 139px; top: 248px; }
  .thanks { left: 139px; top: 349px; }

  .brand {
    position: absolute; z-index: 2; display: flex; align-items: center; gap: 5px;
    color: var(--white); font-size: 11px; line-height: 12px; white-space: nowrap;
  }
  .brand-dot { width: 26px; height: 26px; border-radius: 50%; background: var(--pink-soft); flex: none; }
  .back-brand { left: 213px; top: 386px; }

  .portrait { position: absolute; }
  .back-portrait { left: 304px; top: 202px; width: 256px; height: 277px; }

  .front-cover {
    position: absolute; left: 694px; top: 0; width: 480px; height: 480px; overflow: hidden;
    box-shadow: 3px 4px 5px rgba(0,0,0,.35);
  }
  .title { position: absolute; font-size: 31px; line-height: 1; white-space: nowrap; }
  .title-1 { left: 38px; top: 127px; color: var(--magenta); }
  .title-2 { left: 81px; top: 163px; color: var(--pink-soft); }
  .title-3 { left: 169px; top: 199px; color: var(--white); }
  .author { position: absolute; left: 125px; top: 246px; font-size: 15.5px; color: var(--white); white-space: nowrap; }
  .edition { position: absolute; left: 215px; top: 320px; font-size: 16px; line-height: 21px; color: var(--pink-label); }
  .front-portrait { left: 9px; top: 274px; width: 220px; height: 206px; }
  .front-brand { left: 372px; top: 407px; }
</style>
</head>
<body>
  <section class="back-tray">
    <div class="back-face">
      <div class="network-bg" role="img" aria-label="Violetter Hintergrund mit leuchtendem Netzwerk aus Linien und Punkten"></div>
      <div class="back-copy">
        <p class="intro">Gehen Sie in die Resonanz und<br>finden Sie den richtigen Klienten.<br>Gerne unterstütze ich Sie auf<br>diesem wundervollen Weg.</p>
        <p class="about">Mein Name ist Mirela Gantenbein, ich<br>bin erfolgreiche Unternehmerin, die<br>zugleich spirituell denkt und handelt.<br>Und ich bin fest davon überzeugt.<br>Es gibt eine innere Kraft, die nicht<br>nur Berge versetzt. Sondern auch<br>Ihre Praxis füllt.</p>
        <p class="cd-info">Auf dieser CD werden Sie angeleitet<br>sich mit ihrem Idealkunden zu treffen.<br>Sie werden entdecken welche Probleme<br>oder Herausforderungen, Wünsche und<br>Ziele Ihr potenzieller Klient.</p>
        <p class="thanks">Vielen Dank und viel Spass</p>
      </div>
      <svg class="portrait back-portrait" viewBox="0 0 256 277" role="img" aria-label="Schwarzweiss-Porträt der Autorin in weisser Bluse">
        <defs>
          <linearGradient id="backPhoto" x1="0" y1="0" x2="0" y2="1">
            <stop offset="0" stop-color="var(--photo-dark)"/>
            <stop offset=".45" stop-color="#9a9496"/>
            <stop offset="1" stop-color="var(--photo-light)"/>
          </linearGradient>
        </defs>
        <path d="M80 20 Q130 -5 170 30 L175 140 Q240 160 256 200 L256 277 L0 277 Q40 190 95 160 L75 100 Z" fill="url(#backPhoto)"/>
      </svg>
      <div class="brand back-brand"><span class="brand-dot"></span><span>MGR Online<br>Marketing</span></div>
    </div>
    <span class="spine-label spine-left">Mirela Gantenbein-Rusch</span>
    <span class="spine-label spine-right">Mirela Gantenbein-Rusch</span>
  </section>

  <section class="front-cover">
    <div class="network-bg" role="img" aria-label="Violetter Hintergrund mit leuchtendem Netzwerk aus Linien und Punkten"></div>
    <h1>
      <span class="title title-1">Finde Deinen</span>
      <span class="title title-2">Kompass, Pfad</span>
      <span class="title title-3">der Stille!</span>
    </h1>
    <p class="author">Mirela Gantenbein-Rusch</p>
    <p class="edition">die ÜBUNGS-CD<br>zum Buch</p>
    <svg class="portrait front-portrait" viewBox="0 0 220 206" role="img" aria-label="Porträt der Autorin in violettem Farbton">
      <defs>
        <linearGradient id="frontPhoto" x1="0" y1="0" x2="0" y2="1">
          <stop offset="0" stop-color="#4a1a44"/>
          <stop offset=".5" stop-color="#b08aa8"/>
          <stop offset="1" stop-color="#eedde9"/>
        </linearGradient>
      </defs>
      <path d="M75 10 Q115 -5 150 20 L150 110 Q200 125 215 160 L220 206 L0 206 Q20 150 80 120 L70 70 Z" fill="url(#frontPhoto)"/>
    </svg>
    <div class="brand front-brand"><span class="brand-dot"></span><span>MGR Online<br>Marketing</span></div>
  </section>
</body>
</html>
```